I need a newspaper ads that suits events / outings all over the world. refreshing feeling that suits my company logo.
Size of the ads is 6cm by 6cm a square
takenote
1) Joining up as members is free .
2) Places of interest tickets discount for members
3) Special events / outings host almost everyday
4) main point is everyone able to know each another
website : www.WanderNookly.com
Target Market(s)
Targeting general age 18-40 . mainly singles
contents to put inside the ads
2) Local Places of interest tickets discount for members
4) Website : www.WanderNookly.com
5) We also host photos contest
6) Meet the different faces of the world
7) Experience Sharing Gathering !
Industry/Entity Type
It Company
Requirements
Must have
- Refreshing feeling , and professional . will be uploading more pictures , kindly put some pictures combine into it to make people feel there is a lot activities can be involve when they join as member.

```html
<!DOCTYPE html>
<html lang="en">
<head>
<meta charset="UTF-8">
<title>Orbitra Events – The Gate to the New World</title>
<link href="https://fonts.googleapis.com/css2?family=Bebas+Neue&family=Lato:wght@400;700&display=swap" rel="stylesheet">
<style>
  :root {
    --bg-dark: #2b2b2b;
    --bg-mid: #3a3a3a;
    --footer: #4a4a4a;
    --white: #ffffff;
    --lime: #9fcc3b;
    --periwinkle: #8ea7e3;
    --logo-ink: #2f4a6e;
    --photo-green: #5e7a45;
    --photo-earth: #7c6a55;
    --photo-people: #6b6460;
  }
  * { margin: 0; padding: 0; box-sizing: border-box; }
  html, body { width: 1200px; height: 1200px; overflow: hidden; background: var(--bg-dark); }
  .ad {
    position: relative;
    width: 1200px;
    height: 1200px;
    overflow: hidden;
    background: radial-gradient(ellipse at 40% 60%, var(--bg-mid) 0%, var(--bg-dark) 70%);
    font-family: "Lato", sans-serif;
    color: var(--white);
  }
  .photo { position: absolute; }
  .photo--zoo-feeding {
    left: 0; top: 0; width: 470px; height: 360px;
    background: linear-gradient(160deg, #8c9a6a 0%, var(--photo-green) 45%, var(--photo-earth) 100%);
  }
  .photo--shelter-group {
    left: 460px; top: 0; width: 740px; height: 330px;
    background: linear-gradient(200deg, #4d6b3a 0%, #6f7d5c 50%, #8a8070 100%);
    -webkit-mask-image: linear-gradient(to bottom, #000 70%, transparent 100%);
            mask-image: linear-gradient(to bottom, #000 70%, transparent 100%);
  }
  .photo--friends {
    left: 0; top: 320px; width: 720px; height: 400px;
    background: linear-gradient(180deg, #5a6b52 0%, var(--photo-people) 55%, #4a4542 100%);
    -webkit-mask-image: radial-gradient(ellipse 75% 70% at 45% 45%, #000 55%, transparent 100%);
            mask-image: radial-gradient(ellipse 75% 70% at 45% 45%, #000 55%, transparent 100%);
  }
  .brand {
    position: absolute;
    left: 912px; top: -70px;
    width: 340px; height: 340px;
    border-radius: 50%;
    background: var(--white);
    display: flex; align-items: center; justify-content: flex-start;
    padding-left: 36px; padding-top: 70px;
  }
  .brand__name {
    font-family: "Lato", sans-serif;
    font-weight: 700;
    font-size: 36px;
    line-height: 1.1;
    letter-spacing: 2px;
    color: var(--logo-ink);
    text-align: center;
    width: 220px;
  }
  .headline {
    position: absolute;
    right: 28px; top: 332px;
    font-family: "Bebas Neue", sans-serif;
    text-align: right;
    line-height: 0.84;
    color: var(--white);
  }
  .headline__line { display: block; font-size: 152px; }
  .headline__accent { display: block; font-size: 218px; color: var(--lime); line-height: 0.8; }
  .perks {
    position: absolute;
    left: 64px; top: 736px;
    list-style: none;
  }
  .perks li {
    position: relative;
    padding-left: 32px;
    white-space: nowrap;
  }
  .perks li::before {
    content: "";
    position: absolute;
    left: 0; top: 50%;
    width: 11px; height: 11px;
    margin-top: -5px;
    border-radius: 50%;
    background: var(--white);
  }
  .perks__item--lg { font-size: 44px; color: var(--lime); line-height: 56px; }
  .perks__item--sm { font-size: 25px; color: var(--white); line-height: 42px; }
  .perks__item--sm-blue { font-size: 25px; color: var(--periwinkle); line-height: 42px; }
  .perks__item--md { font-size: 32px; color: var(--white); line-height: 54px; }
  .perks__item--md-blue { font-size: 37px; color: var(--periwinkle); line-height: 54px; }
  .perks__item--lg.spaced { margin-top: 10px; }
  .footer {
    position: absolute;
    left: 0; bottom: 0;
    width: 1200px; height: 92px;
    background: var(--footer);
    display: flex; align-items: center; justify-content: center;
    font-size: 32px;
    color: var(--white);
  }
</style>
</head>
<body>
  <main class="ad">
    <div class="photo photo--zoo-feeding" role="img" aria-label="Member feeding a giraffe at the zoo while a guide talks to the group"></div>
    <div class="photo photo--shelter-group" role="img" aria-label="Group of young members seated together under a wooden shelter in a park"></div>
    <div class="photo photo--friends" role="img" aria-label="Six smiling friends posing together on an outing"></div>

    <div class="brand">
      <span class="brand__name">ORBITRA EVENTS</span>
    </div>

    <h1 class="headline">
      <span class="headline__line">The Gate</span>
      <span class="headline__line">To The</span>
      <span class="headline__line">New</span>
      <span class="headline__accent">World</span>
    </h1>

    <ul class="perks">
      <li class="perks__item--lg">Joining up as members is free</li>
      <li class="perks__item--sm">Local Places of interest tickets discount for members</li>
      <li class="perks__item--sm-blue">Special events / outings host almost everyday</li>
      <li class="perks__item--lg spaced">We also host photos contest</li>
      <li class="perks__item--md">Meet the different faces of the world</li>
      <li class="perks__item--md-blue">Experience Sharing Gathering !</li>
    </ul>

    <footer class="footer">Website : www.WanderNookly.com</footer>
  </main>
</body>
</html>
```